Business Card Design

I need a business card design for a new business based in South West Australia.
I specialize in residential window cleaning & general handyman maintenance.

Industry/Entity Type

Business

Contact Information for Business Card

Dale Marsh - 512 SILVER HAWK DETAILING
- Window Cleaning
- House Maintenance

```html
<!DOCTYPE html>
<html lang="en">
<head>
<meta charset="utf-8">
<title>Dale Marsh – 512 Silver Hawk Detailing</title>
<link href="https://fonts.googleapis.com/css2?family=Source+Sans+3:wght@600;700&display=swap" rel="stylesheet">
<style>
  :root {
    --page-bg: #202329;
    --card-white: #ffffff;
    --brand-blue: #0a5fb0;
    --brand-deep: #0a4f98;
    --accent-cyan: #14a6e8;
    --accent-light: #bfe6fa;
    --text-blue: #0c58a4;
    --contact-blue: #1679c9;
  }
  html, body {
    margin: 0;
    width: 1200px;
    height: 1200px;
    overflow: hidden;
    background: var(--page-bg);
    font-family: "Source Sans 3", "Myriad Pro", Arial, sans-serif;
  }
  .business-card {
    position: absolute;
    left: 50px;
    top: 285px;
    width: 1100px;
    height: 630px;
    background: var(--card-white);
    overflow: hidden;
    box-shadow: 0 20px 50px rgba(0,0,0,0.5);
  }
  .card-art, .card-photo {
    position: absolute;
    left: 0;
    top: 0;
    width: 1100px;
    height: 630px;
  }
  .brand-name {
    position: absolute;
    left: 70px;
    top: 120px;
    width: 300px;
    text-align: center;
    color: var(--card-white);
    font-weight: 700;
    font-size: 38px;
    line-height: 1.05;
    letter-spacing: 1px;
  }
  .brand-mark {
    display: block;
    width: 70px;
    height: 70px;
    margin: 0 auto 18px;
    border-radius: 50%;
    background: var(--card-white);
  }
  .person-name {
    position: absolute;
    left: 150px;
    top: 420px;
    margin: 0;
    color: var(--text-blue);
    font-weight: 700;
    font-size: 72px;
    letter-spacing: 0.5px;
  }
  .contact-list {
    position: absolute;
    left: 630px;
    top: 375px;
    margin: 0;
    padding: 0;
    list-style: none;
    color: var(--contact-blue);
    font-weight: 600;
    font-size: 33px;
  }
  .contact-list li {
    display: flex;
    align-items: center;
    height: 52px;
  }
  .contact-list svg {
    width: 26px;
    height: 26px;
    margin-right: 20px;
    fill: var(--text-blue);
  }
</style>
</head>
<body>
  <div class="business-card">
    <svg class="card-art" viewBox="0 0 1100 630" aria-hidden="true">
      <defs>
        <linearGradient id="topBand" x1="0" y1="0" x2="1" y2="0">
          <stop offset="0" stop-color="#0a5fb0"/>
          <stop offset="1" stop-color="#0b69bd"/>
        </linearGradient>
        <linearGradient id="accentBand" x1="0" y1="0" x2="1" y2="0">
          <stop offset="0" stop-color="#0d9ce6"/>
          <stop offset="0.5" stop-color="#3db8f0"/>
          <stop offset="1" stop-color="#e6f6fd"/>
        </linearGradient>
        <linearGradient id="bottomLight" x1="0" y1="0" x2="1" y2="0">
          <stop offset="0" stop-color="#d8f0fc"/>
          <stop offset="1" stop-color="#5cc3f2"/>
        </linearGradient>
        <linearGradient id="bottomDeep" x1="0" y1="0" x2="1" y2="0">
          <stop offset="0" stop-color="#0a5fb0"/>
          <stop offset="1" stop-color="#12a0e4"/>
        </linearGradient>
      </defs>
      <path d="M0 0 H1100 V170 C900 290 600 340 300 335 C180 333 80 320 0 305 Z" fill="url(#topBand)"/>
      <path d="M0 300 C80 318 180 330 300 332 C600 336 900 290 1100 165 V190 C900 305 600 362 300 362 C180 360 80 350 0 335 Z" fill="url(#accentBand)"/>
      <path d="M0 585 C200 545 430 540 620 562 C420 560 200 590 0 630 Z" fill="url(#bottomLight)"/>
      <path d="M0 612 C200 580 420 566 620 562 C520 578 470 600 440 630 H0 Z" fill="url(#bottomDeep)"/>
    </svg>

    <svg class="card-photo" viewBox="0 0 1100 630" role="img" aria-label="Photo of a hand wiping a window pane with a blue microfibre cloth">
      <defs>
        <linearGradient id="photoTone" x1="0" y1="0" x2="1" y2="0">
          <stop offset="0" stop-color="#0a5fb0" stop-opacity="0"/>
          <stop offset="0.2" stop-color="#3c7fc2" stop-opacity="0.85"/>
          <stop offset="0.5" stop-color="#7fa9cf"/>
          <stop offset="0.75" stop-color="#a9b6bd"/>
          <stop offset="0.9" stop-color="#c8a56a"/>
          <stop offset="1" stop-color="#b98f52"/>
        </linearGradient>
      </defs>
      <path d="M330 0 H1100 V170 C900 290 600 332 330 334 Z" fill="url(#photoTone)"/>
    </svg>

    <div class="brand-name">
      <span class="brand-mark"></span>
      512 SILVER HAWK<br>DETAILING
    </div>

    <h1 class="person-name">Dale Marsh</h1>

    <ul class="contact-list">
      <li>
        <svg viewBox="0 0 24 24" aria-hidden="true"><path d="M6.6 10.8a15.1 15.1 0 0 0 6.6 6.6l2.2-2.2c.3-.3.7-.4 1-.2 1.1.4 2.3.6 3.6.6.6 0 1 .4 1 1V20c0 .6-.4 1-1 1A17 17 0 0 1 3 4c0-.6.4-1 1-1h3.5c.6 0 1 .4 1 1 0 1.3.2 2.5.6 3.6.1.3 0 .7-.2 1z"/></svg>
        048 21 604 37
      </li>
      <li>
        <svg viewBox="0 0 24 24" aria-hidden="true"><path d="M12 3 1 12h3v9h6v-6h4v6h6v-9h3z"/></svg>
        #00, Adress 01, Line 02
      </li>
      <li>
        <svg viewBox="0 0 24 24" aria-hidden="true"><path d="M12 2a10 10 0 1 0 0 20 10 10 0 0 0 0-20zm6.9 6h-3a15 15 0 0 0-1.3-3.9A8 8 0 0 1 18.9 8zM12 4c.8 1.2 1.5 2.5 1.9 4h-3.8c.4-1.5 1.1-2.8 1.9-4zM4.3 14a8 8 0 0 1 0-4h3.4a16 16 0 0 0 0 4zm.8 2h3a15 15 0 0 0 1.3 3.9A8 8 0 0 1 5.1 16zm3-8h-3a8 8 0 0 1 4.3-3.9C8.8 5.3 8.4 6.6 8.1 8zM12 20c-.8-1.2-1.5-2.5-1.9-4h3.8c-.4 1.5-1.1 2.8-1.9 4zm2.3-6H9.7a14 14 0 0 1 0-4h4.6a14 14 0 0 1 0 4zm.3 5.9c.6-1.2 1-2.5 1.3-3.9h3a8 8 0 0 1-4.3 3.9zm1.7-5.9a16 16 0 0 0 0-4h3.4a8 8 0 0 1 0 4z"/></svg>
        emailadress@mail.com
      </li>
    </ul>
  </div>
</body>
</html>
```